A start up Private Wine Label for export to Asia.

We are looking for the best graphic design for our very first wine label Corvessa Cellars and would like the following requirements:

1. Black background - explore and play around the shade of black
2. Gold Shimmery Colour Font
3. Font should be a cursive classic posh that says Corvessa Cellars
4. We would like the front graphic design to be simple and elegant and has a traditional classic feel to it.

Target Market(s)

Small scale to test the upper class market for export to Asia

Font styles to use
Script

Colors

Designer to choose colors to be used in the design.

Requirements
Must have
• Gold font for the label Corvessa Cellars with shimmery touch to it.
• Elegant black background.
• Simple but elegant design.
• Attractive to the upper class market in Asia.
Nice to have
• Explore and play around with your imagination.

```html
<!DOCTYPE html>
<html lang="en">
<head>
<meta charset="utf-8">
<title>Corvessa Cellars — Wine Label</title>
<link href="https://fonts.googleapis.com/css2?family=Pinyon+Script&display=swap" rel="stylesheet">
<style>
  :root {
    --black-light: #2e2e2e;
    --black-deep: #070707;
    --panel-light: #232323;
    --panel-deep: #121212;
    --gold-dark: #a8740f;
    --gold-mid: #d9b23a;
    --gold-light: #f8ec8a;
    --frame-gold: #b9891c;
  }
  * { margin: 0; padding: 0; box-sizing: border-box; }
  html, body { width: 757px; height: 1200px; overflow: hidden; }
  body { background: var(--black-deep); }
  .label {
    position: relative;
    width: 757px;
    height: 1200px;
    background: linear-gradient(90deg, var(--black-light) 0%, #1b1b1b 55%, var(--black-deep) 100%);
  }
  .label__pattern {
    position: absolute;
    left: 49px;
    top: 270px;
    width: 659px;
    height: 660px;
  }
  .label__frame {
    position: absolute;
    left: 49px;
    top: 270px;
    width: 659px;
    height: 660px;
    border: 1.5px solid var(--frame-gold);
  }
  .label__name,
  .label__sub {
    position: absolute;
    left: 0;
    width: 100%;
    text-align: center;
    font-family: "Pinyon Script", cursive;
    font-weight: 400;
    line-height: 1;
    background: linear-gradient(90deg, var(--gold-dark) 0%, var(--gold-mid) 25%, var(--gold-light) 50%, var(--gold-mid) 75%, var(--gold-dark) 100%);
    -webkit-background-clip: text;
    background-clip: text;
    color: transparent;
  }
  .label__name {
    top: 445px;
    font-size: 132px;
    letter-spacing: -1px;
  }
  .label__sub {
    top: 640px;
    left: -16px;
    font-size: 78px;
  }
</style>
</head>
<body>
  <main class="label">
    <svg class="label__pattern" viewBox="0 0 659 660" role="img" aria-label="Art deco geometric line pattern in soft grey on black">
      <defs>
        <linearGradient id="panelFill" x1="0" y1="0" x2="1" y2="0">
          <stop offset="0" stop-color="#262626"/>
          <stop offset="1" stop-color="#141414"/>
        </linearGradient>
      </defs>
      <rect width="659" height="660" fill="url(#panelFill)"/>
    </svg>
    <div class="label__frame"></div>
    <h1 class="label__name">Corvessa</h1>
    <p class="label__sub">Cellars</p>
  </main>
</body>
</html>
```